Psychotherapist need a business card with logo

I am a psychotherapist in need of a business card. The card must have:

Marisol Trevuneda
Psicoterapeuta
937 281 706

Psychologists use the greek letter psy, which is the psychologist symbol, but I would prefer something like a mandala, a graphic symbol, an iconic tree, nothing very usual, but something that shows confidence and trust.

Industry/Entity Type

Business

```html
<!DOCTYPE html>
<html lang="es">
<head>
<meta charset="utf-8">
<title>Marisol Trevuneda · Psicoterapeuta</title>
<link rel="stylesheet" href="https://fonts.googleapis.com/css2?family=Cinzel:wght@400;500&display=swap">
<style>
  :root {
    --backdrop: #2b2b2d;
    --card-orange: #f7931e;
    --card-mid: #f26a21;
    --card-red: #e8321f;
    --ornament-light: #f9a23a;
    --ornament-deep: #ef6a1e;
    --ink: #ffffff;
  }
  html, body {
    margin: 0;
    width: 1200px;
    height: 1200px;
    overflow: hidden;
    background: var(--backdrop);
  }
  .canvas {
    width: 1200px;
    height: 1200px;
    display: flex;
    align-items: center;
    justify-content: center;
  }
  .business-card {
    position: relative;
    width: 1000px;
    height: 572px;
    overflow: hidden;
    background: linear-gradient(90deg, var(--card-orange) 0%, var(--card-mid) 55%, var(--card-red) 100%);
    font-family: "Cinzel", "Times New Roman", serif;
    color: var(--ink);
  }
  .mandala-decoration {
    position: absolute;
    left: -170px;
    top: -150px;
    width: 760px;
    height: 760px;
    border-radius: 50%;
    background: radial-gradient(circle, var(--ornament-light) 0%, var(--ornament-light) 30%, rgba(239,106,30,0.55) 62%, rgba(239,106,30,0) 72%);
  }
  .logo-mark {
    position: absolute;
    left: 640px;
    top: 90px;
    width: 240px;
    display: flex;
    align-items: center;
    gap: 14px;
    font-size: 30px;
    font-weight: 400;
    letter-spacing: 0.06em;
  }
  .logo-mark .logo-dot {
    width: 22px;
    height: 22px;
    border-radius: 50%;
    background: var(--ink);
    flex: none;
  }
  .contact-block {
    position: absolute;
    right: 52px;
    top: 300px;
    text-align: right;
  }
  .holder-name {
    margin: 0;
    font-size: 38px;
    font-weight: 500;
    letter-spacing: 0.04em;
    line-height: 1.1;
  }
  .holder-role {
    margin: 12px 0 0;
    font-size: 30px;
    font-weight: 400;
    letter-spacing: 0.06em;
  }
  .holder-phone {
    margin: 14px 0 0;
    font-size: 30px;
    font-weight: 500;
    letter-spacing: 0.05em;
    display: inline-flex;
    align-items: center;
    gap: 16px;
  }
  .phone-icon { width: 18px; height: 30px; }
</style>
</head>
<body>
<main class="canvas">
  <section class="business-card">
    <div class="mandala-decoration" role="img" aria-label="Orange mandala ornament of looping lines with the Greek letter psi at its centre"></div>

    <div class="logo-mark">
      <span class="logo-dot"></span>
      <span>Trevuneda</span>
    </div>

    <div class="contact-block">
      <h1 class="holder-name">Marisol Trevuneda</h1>
      <p class="holder-role">Psicoterapeuta</p>
      <p class="holder-phone">
        <svg class="phone-icon" viewBox="0 0 18 30" aria-hidden="true">
          <rect x="1.5" y="1.5" width="15" height="27" rx="3" fill="none" stroke="#fff" stroke-width="2.2"/>
          <line x1="1.5" y1="6" x2="16.5" y2="6" stroke="#fff" stroke-width="1.6"/>
          <line x1="1.5" y1="23" x2="16.5" y2="23" stroke="#fff" stroke-width="1.6"/>
        </svg>
        937 281 706
      </p>
    </div>
  </section>
</main>
</body>
</html>
```